Looking for a cool, modern Cannabis Jar Label

I want you to come up with a better, modern look for a label.

I need it sized to 4” x 3” - I plan to print directly to label printer.

I want you to use Photoshop and deliver me a layered PSD file that I can edit and modify the information as needed..

The label information will need to include places for:
(1) Strain Name - most important part of label - larger font size than rest - example Kelvin Thistle, TRP #7, Copperleaf Dunes
(2) Pricing - for Gram, 1/8, 1/4, 1/2. and Ounce
(3) Strain Designation (Hybrid, Indica or Sativa) - maybe color coded, different color for Indica v. Sativa, just an idea
(4) THC and CBD percentages - for example 23% THC and 0.05% CBD
(5) Farm name - a place where we can add the name/logo of the business that produced the product. example - Brosk Farms

I have attached a simple mockup showing the information.

I have also attached a few samples of labels we like to give you an idea of the look and feel we are going for.

I am wanting a very clean, modern, classy, readable look.The font will use is Gotham Font.

HI Everyone! Thank you for all of your designs. I am requesting an extension because I need more time to give adequate feedback to the designers. Thank you for your participation and all of your efforts! I will be making a decision soon!

• Gotham Font

• Thank you for your designs. I am sorry i have been slow in providing feedback, things have been really busy around here!
• I wanted to give some group general feedback. After reviewing all of the designs, there is a common theme among all of the designs that I would like to see changed.
• I would like to see the per gram pricing more prominent on the label. This is what most people are looking for when they are purchasing the product. So I would like to see this stand out from the other pricing tiers. As I think about it, they don't all need to be grouped together in a line. You could have the Per Gram pricing front and center some where and then the other pricing tiers grouped together somewhere else on the label.
• This is the order of importance of items on the label. Items at the the top of the list should be bigger than those below it.
• 1. Strain name
• 2. Pricing - being per gram the most important of all prices
• 3. THC/CBD percentages
• 4. Strain Type (indica, sativa, hybrid)
• 5. Farm name/logo
• When laying out these labels, they will be going on rounded jars and they will be on display. Think of jars with fancy labels in a candy store. They need to be eye catchy, appealing, but easy read.
• Thank you for all of your hard work, everyone is doing a great job.
• Best,
• Neta

```html
<!DOCTYPE html>
<html lang="en">
<head>
<meta charset="utf-8">
<title>Jar Label Concepts – Juniper Ridge Frost</title>
<link href="https://fonts.googleapis.com/css2?family=Montserrat:wght@500;600;700;800&display=swap" rel="stylesheet">
<style>
  :root {
    --brown: #5b5146;
    --orange: #f7941d;
    --cream: #f2deb7;
    --white: #ffffff;
    --ink: #4a4238;
  }
  * { box-sizing: border-box; margin: 0; padding: 0; }
  html, body {
    width: 1200px; height: 369px; overflow: hidden;
    background: var(--white);
    font-family: "Montserrat", Arial, sans-serif;
  }
  .board { position: relative; width: 1200px; height: 369px; }

  .concept { position: absolute; top: 51px; width: 338px; }
  .concept--a { left: 39px; }
  .concept--b { left: 410px; }
  .concept--c { left: 798px; }

  .concept__letter {
    position: absolute; top: 271px; left: 0; width: 100%;
    text-align: center; font-weight: 700; font-size: 22px; color: var(--brown);
  }

  .label {
    width: 338px; height: 254px;
    background: var(--orange);
    display: flex; flex-direction: column; gap: 6px;
  }

  /* Strain name header */
  .label__header {
    position: relative; height: 83px; background: var(--brown);
    display: flex; align-items: center; justify-content: center;
    text-align: center; color: var(--white);
  }
  .strain-name {
    position: relative; z-index: 1;
    font-family: inherit; font-weight: 700; font-size: 30px; line-height: 34px;
    letter-spacing: 0.5px; white-space: nowrap;
  }
  .label--framed .label__header::after {
    content: ""; position: absolute; inset: 5px 5px 0 5px;
    border: 2.5px solid var(--orange);
  }
  .stripes { position: absolute; top: 9px; display: flex; flex-direction: column; gap: 10.5px; }
  .stripes--left { left: 0; }
  .stripes--right { right: 0; }
  .stripes span { display: block; width: 22px; height: 8px; background: var(--orange); }

  /* Price row */
  .label__prices {
    height: 65px; display: grid;
    grid-template-columns: 58fr 61fr 64fr 67fr 74fr; column-gap: 3px;
  }
  .price {
    background: var(--brown); color: var(--white);
    display: flex; flex-direction: column; align-items: center; justify-content: center;
  }
  .price--gram { background: var(--cream); color: var(--brown); }
  .price__amount { font-weight: 700; font-size: 24px; line-height: 26px; }
  .price__unit { font-weight: 500; font-size: 11.5px; line-height: 16px; letter-spacing: 0.2px; }

  /* Bottom section */
  .label__details { flex: 1; display: flex; gap: 3px; }
  .details__left { width: 170px; display: flex; flex-direction: column; }
  .potency {
    position: relative; height: 56px; background: var(--orange);
    display: grid; grid-template-columns: 84fr 81fr; column-gap: 3px;
  }
  .potency__cell {
    background: var(--cream); color: var(--brown);
    display: flex; flex-direction: column; align-items: center; justify-content: center;
    font-weight: 700; font-size: 20px; line-height: 21px; text-align: center;
  }
  .notch { position: absolute; top: 21px; width: 0; height: 0; border-top: 7px solid transparent; border-bottom: 7px solid transparent; }
  .notch--in { left: 0; border-left: 8px solid var(--orange); }
  .notch--out { right: 0; border-right: 8px solid var(--orange); }
  .notch--mid { left: 79px; top: 22px; width: 13px; height: 13px; background: var(--orange); transform: rotate(45deg); border: 0; }

  .strain-type {
    flex: 1; background: var(--brown); color: var(--white);
    display: flex; align-items: center; justify-content: center;
    font-weight: 700; font-size: 22px; letter-spacing: 0.5px;
  }
  .farm {
    flex: 1; background: var(--cream);
    display: flex; align-items: center; justify-content: center; gap: 8px;
  }
  .farm__dot { width: 30px; height: 30px; border-radius: 50%; border: 2px solid var(--ink); }
  .farm__name { font-weight: 800; font-size: 16px; line-height: 18px; color: var(--ink); letter-spacing: 0.5px; }
</style>
</head>
<body>
<main class="board">

  <section class="concept concept--a">
    <article class="label">
      <header class="label__header"><h1 class="strain-name">JUNIPER RIDGE<br>FROST</h1></header>
      <div class="label__prices">
        <div class="price price--gram"><span class="price__amount">$10</span><span class="price__unit">GRAM</span></div>
        <div class="price"><span class="price__amount">$35</span><span class="price__unit">EIGHTH</span></div>
        <div class="price"><span class="price__amount">$70</span><span class="price__unit">QUARTER</span></div>
        <div class="price"><span class="price__amount">$140</span><span class="price__unit">HALF</span></div>
        <div class="price"><span class="price__amount">$280</span><span class="price__unit">OUNCE</span></div>
      </div>
      <div class="label__details">
        <div class="details__left">
          <div class="potency">
            <div class="potency__cell">28%<br>THC</div>
            <div class="potency__cell">2%<br>CBD</div>
            <span class="notch notch--in"></span><span class="notch notch--mid"></span><span class="notch notch--out"></span>
          </div>
          <div class="strain-type">INDICA</div>
        </div>
        <div class="farm"><span class="farm__dot"></span><span class="farm__name">BROSK<br>FARMS</span></div>
      </div>
    </article>
    <p class="concept__letter">A</p>
  </section>

  <section class="concept concept--b">
    <article class="label label--framed">
      <header class="label__header"><h1 class="strain-name">JUNIPER RIDGE<br>FROST</h1></header>
      <div class="label__prices">
        <div class="price price--gram"><span class="price__amount">$10</span><span class="price__unit">GRAM</span></div>
        <div class="price"><span class="price__amount">$35</span><span class="price__unit">EIGHTH</span></div>
        <div class="price"><span class="price__amount">$70</span><span class="price__unit">QUARTER</span></div>
        <div class="price"><span class="price__amount">$140</span><span class="price__unit">HALF</span></div>
        <div class="price"><span class="price__amount">$280</span><span class="price__unit">OUNCE</span></div>
      </div>
      <div class="label__details">
        <div class="details__left">
          <div class="potency">
            <div class="potency__cell">28%<br>THC</div>
            <div class="potency__cell">2%<br>CBD</div>
            <span class="notch notch--in"></span><span class="notch notch--mid"></span><span class="notch notch--out"></span>
          </div>
          <div class="strain-type">INDICA</div>
        </div>
        <div class="farm"><span class="farm__dot"></span><span class="farm__name">BROSK<br>FARMS</span></div>
      </div>
    </article>
    <p class="concept__letter">B</p>
  </section>

  <section class="concept concept--c">
    <article class="label label--striped">
      <header class="label__header">
        <div class="stripes stripes--left"><span></span><span></span><span></span><span></span></div>
        <h1 class="strain-name">JUNIPER RIDGE<br>FROST</h1>
        <div class="stripes stripes--right"><span></span><span></span><span></span><span></span></div>
      </header>
      <div class="label__prices">
        <div class="price price--gram"><span class="price__amount">$10</span><span class="price__unit">GRAM</span></div>
        <div class="price"><span class="price__amount">$35</span><span class="price__unit">EIGHTH</span></div>
        <div class="price"><span class="price__amount">$70</span><span class="price__unit">QUARTER</span></div>
        <div class="price"><span class="price__amount">$140</span><span class="price__unit">HALF</span></div>
        <div class="price"><span class="price__amount">$280</span><span class="price__unit">OUNCE</span></div>
      </div>
      <div class="label__details">
        <div class="details__left">
          <div class="potency">
            <div class="potency__cell">28%<br>THC</div>
            <div class="potency__cell">2%<br>CBD</div>
            <span class="notch notch--in"></span><span class="notch notch--mid"></span><span class="notch notch--out"></span>
          </div>
          <div class="strain-type">INDICA</div>
        </div>
        <div class="farm"><span class="farm__dot"></span><span class="farm__name">BROSK<br>FARMS</span></div>
      </div>
    </article>
    <p class="concept__letter">C</p>
  </section>

</main>
</body>
</html>
```